Flyer-Design für nachhaltige Familienberatung
Reiche Ideenvielfalt (viele sehr verschiedene Designvorschläge), prompte Umsetzung aller Änderungsideen während und nach dem Wettbewerb und dazu ein sehr freundlicher Kontakt - so macht die Zusammenarbeit wirklich Spaß! Vielen Dank dafür!
Zielgruppe
Ich bin Kleinunternehmerin und berate junge Familien (auch Schwangere, Alleinerziehende und andere Angehörige) zu den Themen Stoffwindeln, Windelfrei, Babyschlaf und bedürfnis-/bindungsorientierter Erziehung. Außerdem biete ich Paarberatung und Einzelcoaching für Mütter und - gemeinsam mit meinem Mann - für Väter an.
Der Name 'Familie MiTi' steht für Mirja und Till, mich und meinem Mann, gleichzeitig ein Wortspiel mit einer 'Hasenfamilie', auf das gern angespielt werden kann.
Weitere Informationen zum Angebot können der Internetseite www.familie-miti.example entnommen werden.
Aufgabenstellung
Das Design sollte farblich und stilistisch zum Logo passen. Naturverbundenheit/Nachhaltigkeit und Familienleben/Geborgenheit dürfen im Mittelpunkt stehen.
Mein Angebot ist vielfältig - umso wichtiger ist eine übersichtliche klare Darstellung. Der Flyer sollte junge Familien ansprechen. Er sollte hochwertig und liebevoll wirken: die Leser*innen sollten ermutigt werden, mich einfach unverbindlich anzurufen/mir zu schreiben (E-Mail, Signal, WhatsApp, Facebook-Messenger) und mehr über das Angebot zu erfahren.
Die Flyer werden vor allem in Geburtshäusern, Krankenhäusern, Familienzentren und bei Frauen-/Kinderärzt*innen und Hebammen ausliegen. Außerdem werden sie durch Kooperationspartner*innen (Still-/Trageberaterinnen, in Geburtsvorbereitungskursen) verteilt.
Die hochgeladenen Fotos dürfen, müssen aber nicht verwendet werden.

```html
<!DOCTYPE html>
<html lang="de">
<head>
<meta charset="utf-8">
<title>Familie MiTi – Familienberatung Flyer</title>
<link href="https://fonts.googleapis.com/css2?family=Montserrat:wght@300;400&family=Quicksand:wght@400;500&display=swap" rel="stylesheet">
<style>
  :root {
    --bg: #e6e6e4;
    --paper: #ffffff;
    --ink: #2b2b2b;
    --ink-soft: #3a3a3a;
    --grey: #6d6d6d;
    --orange: #e2782a;
    --sage: #d9eadb;
    --peach: #f5e0d2;
    --photo-blue: #3a5b94;
    --photo-brown: #8a5a32;
    --photo-green: #6f8f3e;
    --photo-cream: #ece3d3;
  }
  * { margin: 0; padding: 0; box-sizing: border-box; }
  html, body { width: 1200px; height: 900px; overflow: hidden; }
  body { background: var(--bg); position: relative; font-family: "Quicksand", sans-serif; color: var(--ink); }

  .page {
    position: absolute; top: 45px; width: 540px; height: 810px;
    background: var(--paper);
    box-shadow: 0 10px 30px rgba(0,0,0,0.12);
  }
  .page--front { left: 40px; }
  .page--back { left: 620px; }
  .page__art { position: absolute; inset: 0; width: 100%; height: 100%; }

  /* front */
  .brand { position: absolute; top: 448px; left: 0; width: 100%; text-align: center; }
  .brand__dot { width: 54px; height: 54px; border-radius: 50%; background: var(--sage); margin: 0 auto 8px; }
  .brand__name { font-family: "Montserrat", sans-serif; font-weight: 400; font-size: 13px; letter-spacing: 1px; color: var(--orange); }

  .title { position: absolute; top: 549px; width: 100%; text-align: center;
    font-family: "Montserrat", sans-serif; font-weight: 400; font-size: 47px; letter-spacing: 1.5px; color: var(--ink); }
  .subtitle { position: absolute; top: 611px; width: 100%; text-align: center;
    font-family: "Montserrat", sans-serif; font-weight: 300; font-size: 18px; letter-spacing: 1.2px; color: var(--grey); }
  .services { position: absolute; top: 661px; left: 0; width: 100%; display: flex; justify-content: center; list-style: none;
    font-family: "Montserrat", sans-serif; font-weight: 300; font-size: 17px; color: var(--ink); }
  .services li { padding: 3px 16px; }
  .services li + li { border-left: 1.5px solid var(--orange); }
  .intro { position: absolute; top: 711px; left: 60px; width: 415px; font-size: 12.3px; line-height: 18.5px; color: var(--ink-soft); }

  /* back */
  .motto { position: absolute; top: 278px; right: 46px; text-align: right;
    font-family: "Montserrat", sans-serif; font-weight: 300; font-size: 15.5px; line-height: 20px; letter-spacing: 0.8px; color: var(--grey); }
  .mission { position: absolute; top: 338px; left: 207px; width: 288px; font-size: 11.3px; line-height: 17px; color: var(--ink-soft); }
  .mission p { text-align: justify; text-align-last: right; }
  .contact { position: absolute; top: 545px; right: 46px; text-align: right; font-size: 11.3px; line-height: 17px; color: var(--ink-soft); font-style: normal; }
  .contact__block + .contact__block { margin-top: 17px; }
</style>
</head>
<body>

<section class="page page--front">
  <svg class="page__art" viewBox="0 0 735 1102" preserveAspectRatio="none">
    <defs>
      <linearGradient id="sleepTones" x1="0" y1="0" x2="1" y2="1">
        <stop offset="0" stop-color="#b9b6b2"/>
        <stop offset="0.35" stop-color="var(--photo-brown)"/>
        <stop offset="0.7" stop-color="var(--photo-blue)"/>
        <stop offset="1" stop-color="#2e4c84"/>
      </linearGradient>
    </defs>
    <g role="img" aria-label="Foto: schlafendes Kind im Sternenschlafanzug mit Teddybär">
      <polygon points="0,58 366,58 150,182 0,104" fill="url(#sleepTones)"/>
      <polygon points="378,58 735,58 735,120 594,190" fill="url(#sleepTones)"/>
      <polygon points="372,80 590,200 590,452 372,572 152,452 152,200" fill="url(#sleepTones)"/>
      <polygon points="0,116 146,200 146,452 0,535" fill="url(#sleepTones)"/>
      <polygon points="735,126 598,200 598,452 735,535" fill="url(#sleepTones)"/>
    </g>
  </svg>

  <div class="brand">
    <div class="brand__dot"></div>
    <div class="brand__name">FAMILIE MITI</div>
  </div>
  <h1 class="title">Familienberatung</h1>
  <p class="subtitle">SPEZIELL FÜR SIE</p>
  <ul class="services">
    <li>Begleitung</li>
    <li>Workshops</li>
    <li>Beratung</li>
  </ul>
  <p class="intro">Wir möchten euch unterstützen, einen natürlichen und für euch passenden Weg als Familie zu finden. Egal, ob ein Kind oder viele, alleinerziehend oder Regenbogenfamilie, jeder ist willkommen.</p>
</section>

<section class="page page--back">
  <svg class="page__art" viewBox="0 0 735 1102" preserveAspectRatio="none">
    <defs>
      <linearGradient id="meadowTones" x1="0" y1="0" x2="0" y2="1">
        <stop offset="0" stop-color="#9bb06a"/>
        <stop offset="0.5" stop-color="var(--photo-green)"/>
        <stop offset="1" stop-color="#4f7a2c"/>
      </linearGradient>
      <linearGradient id="newbornTones" x1="0" y1="0" x2="1" y2="1">
        <stop offset="0" stop-color="#d8cdbd"/>
        <stop offset="0.5" stop-color="var(--photo-cream)"/>
        <stop offset="1" stop-color="#d9c8ae"/>
      </linearGradient>
    </defs>
    <polygon class="deco-hex" points="152,58 425,58 425,165 288,242 152,165" fill="var(--sage)"/>
    <polygon class="deco-hex" points="0,410 138,488 138,642 0,722" fill="var(--sage)"/>
    <polygon class="deco-hex" points="285,902 421,978 421,1102 148,1102 148,978" fill="var(--peach)"/>
    <polygon role="img" aria-label="Foto: krabbelndes Kleinkind mit Stoffwindel auf einer Blumenwiese" points="145,170 282,248 282,405 145,482 8,405 8,248" fill="url(#meadowTones)"/>
    <polygon role="img" aria-label="Foto: schlafendes Neugeborenes mit Kuscheltier" points="145,658 282,735 282,893 145,970 8,893 8,735" fill="url(#newbornTones)"/>
  </svg>

  <h2 class="motto">NATÜRLICH<br>MENSCH SEIN</h2>
  <div class="mission">
    <p>Wir wünschen uns eine Gesellschaft, in der Menschen sich respektieren und Vertrauen zueinander, als auch zu sich selbst haben. Eine Gesellschaft, in der Kinder gut aufwachsen können. Deshalb möchten wir Eltern stärken, ihnen zur Seite stehen und ggf. Informationen an die Hand geben, die ihnen in ihrer aktuellen Situation helfen.</p>
    <p>Wir möchten Familien ermutigen, für sich als Einzelpersonen und als Familienverbund einzustehen und den Weg zu gehen, der für genau sie genau jetzt passt.</p>
  </div>
  <address class="contact">
    <div class="contact__block">Familie MiTi<br>Mirja Welkert<br>Birkenweg 5<br>37000 Wiesental</div>
    <div class="contact__block">0151 - 23456789<br>mirja@familie-miti.example<br>www.familie-miti.example</div>
  </address>
</section>

</body>
</html>
```